Thimble Deli Needs a Web Page!

Thimble Deli is a gourmet sandwich shop in Baltimore, MD USA.
We are due to open in about a month or so and we need a great web page that looks cool and is easy to use. Our Concept supports local farmers, ranchers, fishmongers & purveyors. All of our menu items are made from scratch using fresh local ingredients.

Target Market(s)

Urban people on the go & Anyone who is hungry and likes a great sandwich

Industry/Entity Type

Shop

Requirements
Must have
• We must have these 8 tabs:
Home
Menus
Gallery
About Us
Media & Events
Hours & Location
Order Online
Contact Us

Also we would like our Logo to be a focal point
Our Color scheme is Red, Black, Grey, White and a reddish-orange
however any and all colors are great and will be considered
We would love an area on the page for our own food photos to be added.
Nice to have
• Baltimore Skyline
Order Online Now Button
Free Wi-Fi Symbol
Dine-In, Take Out, Delivery,
Business Lunches, Tail Gate Platters, Catering
Should not have
• No Stock images of food or chefs.
(We want to put all of our own food photos up later.)
No Pink.

```html
<!DOCTYPE html>
<html lang="en">
<head>
<meta charset="utf-8">
<title>Thimble Deli</title>
<link href="https://fonts.googleapis.com/css2?family=Ubuntu:ital,wght@0,400;0,500;0,700;1,400&display=swap" rel="stylesheet">
<style>
:root{
  --red-deep:#8c0b10;
  --red:#b5141a;
  --red-bright:#c9161d;
  --orange:#d2561c;
  --brown:#a9401a;
  --text:#8c1515;
  --cream:#fbeee2;
  --line:#e8c9c4;
  --white:#ffffff;
  --font:"Ubuntu",Arial,sans-serif;
}
*{margin:0;padding:0;box-sizing:border-box}
html,body{width:814px;height:1200px;overflow:hidden}
body{position:relative;background:var(--white);font-family:var(--font);color:var(--text)}
.abs{position:absolute}

.masthead{left:0;top:0;width:814px;height:380px;
  background:linear-gradient(180deg,#9d0f14 0%,#b51d18 40%,#c9441b 80%,#d2561c 100%);
  border-top:3px solid #fff}
.brand{left:55px;top:22px;display:flex;align-items:center;gap:8px}
.brand-dot{width:22px;height:22px;border-radius:50%;background:var(--white)}
.brand-name{font-size:24px;font-weight:700;color:var(--white);line-height:1}
.skyline{left:279px;top:26px;width:483px;height:78px;border:2px solid var(--white);
  background:linear-gradient(180deg,#6d7b93 0%,#8d7b72 45%,#c2763f 70%,#2b2a33 100%)}

.main-nav{left:53px;top:122px;width:709px;height:39px;background:var(--red-deep);
  display:flex;border-radius:3px 3px 0 0;overflow:hidden}
.main-nav a{color:var(--white);text-decoration:none;font-size:12.5px;line-height:39px;
  text-align:center;border-right:1px solid #a52a2e;white-space:nowrap;flex:none}
.main-nav a:last-child{border-right:0}
.main-nav a.active{background:var(--red-bright);font-weight:500}
.w66{width:66px}.w69{width:69px}.w80{width:80px}.w111{width:111px}.w117{width:117px}.w98{width:98px}.w102{width:102px}

.stage{left:53px;top:161px;width:709px;height:256px;background:#f1efee;box-shadow:0 6px 8px -6px rgba(0,0,0,.35)}
.slide{left:61px;top:168px;width:690px;height:239px;
  background:linear-gradient(120deg,#8d8a6a 0%,#b87a3a 35%,#c8493a 55%,#d9c4a8 75%,#6f6a60 100%)}
.slide-arrow{top:268px;width:22px;height:40px;background:rgba(255,255,255,.9);border-radius:4px;
  display:flex;align-items:center;justify-content:center}
.slide-arrow.prev{left:61px}
.slide-arrow.next{left:730px}
.slide-dots{left:671px;top:385px;display:flex;gap:2px}
.slide-dots span{width:17px;height:16px;font-size:11px;color:#eee;background:rgba(60,60,60,.75);
  display:flex;align-items:center;justify-content:center}
.slide-dots span.on{background:#fff;color:#333}

.welcome{left:54px;top:434px;width:480px}
.section-title{font-size:16px;font-weight:400;color:#a0141a}
.welcome .section-title{margin-bottom:10px}
.welcome-thumb{float:left;width:131px;height:65px;margin:0 6px 4px 0;border:1px solid #ccc;
  background:linear-gradient(135deg,#c9b08e,#f0e4d2 50%,#8d6a4a)}
.welcome p{font-size:8.5px;line-height:13px;margin-bottom:4px}

.promo{left:549px;width:209px;border:1px solid #d88;border-radius:3px;background:#fff;
  box-shadow:0 0 0 2px #f6e6e4}
.order-box{top:437px;height:101px;padding:9px 8px 9px 13px}
.order-box h3{font-size:15px;font-weight:500;color:#a0141a;margin-bottom:3px}
.order-box p{font-size:8px;line-height:12px;white-space:nowrap}
.order-btn{position:absolute;left:13px;top:62px;background:var(--red);color:#fff;font-size:11px;
  padding:6px 9px;border-radius:12px;line-height:12px}
.order-mouse{position:absolute;left:118px;top:55px}
.wifi-box{top:546px;height:86px;display:flex;align-items:center;justify-content:center;gap:24px}
.wifi-badge{background:var(--red);color:#fff;font-weight:700;font-size:15px;padding:10px 13px;border-radius:22px;line-height:1}

.rule{left:53px;top:650px;width:706px;height:1px;background:var(--line)}

.gallery-title{left:55px;top:671px}
.gallery{left:53px;top:701px;display:flex;gap:10px}
.gallery-item{width:169px;height:95px;padding:4px;background:#fff;border:1px solid #ddd;box-shadow:0 1px 3px rgba(0,0,0,.15)}
.gallery-item div{width:100%;height:100%}
.g1{background:linear-gradient(135deg,#2d2b30,#8a6a55 50%,#d7c6b6)}
.g2{background:linear-gradient(135deg,#d9b07a,#b5733a 50%,#e8dcc7)}
.g3{background:linear-gradient(135deg,#b5422a,#d98a4a 50%,#8a2a1e)}
.g4{background:linear-gradient(135deg,#c9a25a,#8a3a1a 50%,#e8d9b0)}

.lower{left:0;top:831px;width:814px;height:261px;background:linear-gradient(180deg,#fbe8d9,#fff6ef 40%,#fcf3ec)}
.lower::before{content:"";position:absolute;left:0;top:-6px;width:100%;height:12px;
  background:radial-gradient(circle at 10px 12px,#fbe8d9 9px,transparent 10px) repeat-x;background-size:20px 12px}
.col{top:852px}
.col .section-title{margin-bottom:12px}
.blog{left:54px;width:214px}
.blog-item{display:flex;gap:7px;margin-bottom:20px}
.blog-thumb{flex:none;width:73px;height:65px;border:1px solid #a0141a;border-radius:4px}
.blog-thumb.t1{background:linear-gradient(135deg,#c89a3a,#3a4a8a 50%,#d9c8b0)}
.blog-thumb.t2{background:linear-gradient(135deg,#3a2a20,#d9c08a 50%,#f0e8d8)}
.blog-item h4{font-size:10.5px;font-weight:400;color:#8c1010;margin-bottom:5px}
.blog-item p{font-size:8.5px;line-height:12px}
.divider{top:858px;width:0;height:215px;border-left:1px dashed #d9a9a0}
.testimonials{left:292px;width:218px}
.testimonials blockquote{font-style:italic;font-size:8.5px;line-height:13.5px;margin-bottom:6px}
.testimonials cite{display:block;font-style:normal;font-size:10px;margin-bottom:16px}
.testimonials cite b{font-weight:700}
.news{left:548px;width:214px}
.news h4{font-size:10.5px;font-weight:400;color:#8c1010}
.news time{display:block;font-size:10px;margin-bottom:7px}
.news p{font-size:8.5px;line-height:13px;margin-bottom:18px}
.view-more{top:1049px;width:210px;height:22px;font-size:12px;color:#8c1010;padding:3px 12px;
  background:linear-gradient(90deg,#f4dccb,rgba(244,220,203,0));border-radius:4px 0 0 4px}

.site-footer{left:0;top:1092px;width:814px;height:108px;background:linear-gradient(180deg,#a9401a,#a3371a)}
.footer-nav{left:46px;top:1110px;display:flex;font-size:9.5px;color:#fff}
.footer-nav span{padding:0 6px;border-left:1px solid #e9b8a0;line-height:11px}
.footer-nav span:first-child{border-left:0;padding-left:0}
.legal{left:46px;top:1134px;font-size:8.5px;color:#f5d9cc}
.footer-brand{left:664px;top:1116px;display:flex;align-items:center;gap:5px}
.footer-brand .brand-dot{width:12px;height:12px}
.footer-brand .brand-name{font-size:13px}
</style>
</head>
<body>
<header class="abs masthead"></header>
<div class="abs brand"><span class="brand-dot"></span><span class="brand-name">Thimble Deli</span></div>
<div class="abs skyline" role="img" aria-label="City skyline at dusk over the harbour"></div>

<nav class="abs main-nav">
  <a class="active w66" href="#">Home</a><a class="w66" href="#">Menus</a><a class="w69" href="#">Gallery</a><a class="w80" href="#">About Us</a><a class="w111" href="#">Media &amp; Events</a><a class="w117" href="#">Hours &amp; Location</a><a class="w98" href="#">Order Online</a><a class="w102" href="#">Contact Us</a>
</nav>

<div class="abs stage"></div>
<div class="abs slide" role="img" aria-label="Buffet table with fresh salads being served"></div>
<div class="abs slide-arrow prev"><svg width="8" height="16"><path d="M1 1 L7 8 L1 15" fill="none" stroke="#555" stroke-width="1.5"/></svg></div>
<div class="abs slide-arrow next"><svg width="8" height="16"><path d="M7 1 L1 8 L7 15" fill="none" stroke="#555" stroke-width="1.5"/></svg></div>
<div class="abs slide-dots"><span class="on">1</span><span>2</span><span>3</span><span>4</span></div>

<section class="abs welcome">
  <h2 class="section-title">Welcome to Thimble Deli Website Mainpage !</h2>
  <div class="welcome-thumb" role="img" aria-label="Dining room with set tables"></div>
  <p>Brightleaf Studio is a web service company, offering a wide range of services which range from designing and development, that is covering almost all the fields in the best possible way.</p>
  <p>To be the best we know what and how to present beautifully the working of the client's need and their advantages be highlighted.</p>
  <p>Thus, Wanna get ahead in the competition with other websites…. Brightleaf Studio provide you with an attractive and most convincing website to enhance your marketing goals.</p>
  <p>The only way to success is through the right path and that's what we provide you. None of the other companies has the result we do. So stick to the best that's how you will be the best don't opt for the second best. Our expertise does not limit itself to web development but also it includes Web Hosting, Search Engine Optimization, E-Commerce. We partner hundreds of organization to enhance their business, marketing and profit goals.</p>
</section>

<aside class="abs promo order-box">
  <h3>Online Order Now</h3>
  <p>To be the best we know what and how to present<br>beautifully the working of the client's need</p>
  <span class="order-btn">Online Order Now</span>
  <svg class="order-mouse" width="22" height="38" viewBox="0 0 22 38"><path d="M0 14 Q6 14 8 8" fill="none" stroke="#b5141a" stroke-width="1.3"/><rect x="6" y="10" width="14" height="26" rx="7" fill="none" stroke="#b5141a" stroke-width="1.3"/><line x1="13" y1="10" x2="13" y2="19" stroke="#b5141a" stroke-width="1.3"/></svg>
</aside>
<aside class="abs promo wifi-box">
  <span class="wifi-badge">Free Wi-Fi</span>
  <svg width="62" height="66" viewBox="0 0 62 66"><g fill="none" stroke="#b5141a" stroke-width="3" stroke-linecap="round"><path d="M19 14 Q13 21 19 28"/><path d="M43 14 Q49 21 43 28"/><path d="M12 7 Q2 21 12 35"/><path d="M50 7 Q60 21 50 35"/><path d="M5 2 Q-8 21 5 40"/><path d="M57 2 Q70 21 57 40"/></g><circle cx="31" cy="21" r="4" fill="#b5141a"/><path d="M31 24 L22 64 L40 64 Z" fill="#b5141a"/></svg>
</aside>

<div class="abs rule"></div>

<h2 class="abs section-title gallery-title">Speical Foods Gallery</h2>
<div class="abs gallery">
  <div class="gallery-item"><div class="g1" role="img" aria-label="Guests serving themselves at a buffet"></div></div>
  <div class="gallery-item"><div class="g2" role="img" aria-label="Platters of catered food"></div></div>
  <div class="gallery-item"><div class="g3" role="img" aria-label="Tray of sandwiches"></div></div>
  <div class="gallery-item"><div class="g4" role="img" aria-label="Burger with fries and a drink"></div></div>
</div>

<div class="abs lower"></div>

<section class="abs col blog">
  <h2 class="section-title">Recent Blog</h2>
  <article class="blog-item"><div class="blog-thumb t1" role="img" aria-label="Kitchen scene"></div><div><h4>Tittle goes here</h4><p>Brightleaf Studio provide you with an attractive and most convincing website to enhance your marketing goals.</p></div></article>
  <article class="blog-item"><div class="blog-thumb t2" role="img" aria-label="Glasses on a dining table"></div><div><h4>Tittle goes here</h4><p>Brightleaf Studio provide you with an attractive and most convincing website to enhance your marketing goals.</p></div></article>
</section>
<div class="abs divider" style="left:276px"></div>
<section class="abs col testimonials">
  <h2 class="section-title">Testimonials</h2>
  <blockquote>To be the best we know what and how to present beautifully the working of the client's need and their advantages be highlighted. We act in accordance with the Industry certified processes to deliver the best to our clients all over the world.</blockquote>
  <cite>By <b>Author Name</b></cite>
  <blockquote>To be the best we know what and how to present beautifully the working of the client's need and their advantages be highlighted.</blockquote>
  <cite>By <b>Author Name</b></cite>
</section>
<div class="abs divider" style="left:529px"></div>
<section class="abs col news">
  <h2 class="section-title">News &amp; Events</h2>
  <h4>Headline goes here</h4><time>20.March.2012</time>
  <p>To be the best we know what and how to present beautifully the working of the client's need and their advantages be highlighted.</p>
  <h4>Headline goes here</h4><time>20.March.2012</time>
  <p>To be the best we know what and how to present beautifully the working of the client's need and their advantages be highlighted.</p>
</section>
<a class="abs view-more" style="left:43px">view more ›</a>
<a class="abs view-more" style="left:294px">view more ›</a>
<a class="abs view-more" style="left:545px">view more ›</a>

<footer class="abs site-footer"></footer>
<nav class="abs footer-nav"><span>Home</span><span>Menus</span><span>Gallery</span><span>About Us</span><span>Media &amp; Events</span><span>Hours &amp; Location</span><span>Order Online</span><span>Contact Us</span></nav>
<p class="abs legal">© 2012 Company Name &nbsp;|&nbsp; All right reserved &nbsp;|&nbsp; Term &amp; Conditions</p>
<div class="abs footer-brand"><span class="brand-dot"></span><span class="brand-name">Thimble Deli</span></div>
</body>
</html>
```